Design a modern, premium front panel for a stand-up pouch

Design a modern, premium front for a stand-up pouch for VELUTRA. Product is for Urine/vomit/runny stool incidents indoors; quick cleanups before smell sets; nighttime/elderly pet accidents; travel/car mishaps.

It must instantly show it’s for dogs & cats and include three small step icons with labels: Sprinkle → Wait 1–5 min → Sweep. Front copy to include: VELUTRA, descriptor “Mineral Instant Absorber – for Dogs & Cats”, one benefits line “Fragrance-Free • 100 % Mineral • Odor-Binding • Low-Dust

Goal: clear who/what/how in under 3 seconds
Deliverables: AI/PDF + a pouch mockup;

Target Market(s)

• Dog & cat households in apartments/homes; new pet parents, senior pets, multi-pet homes. • Cleanliness & odor-sensitive buyers (allergies/asthma, fragrance-free preference). • Surfaces at risk: carpets/rugs, sofas, mattresses, car interiors.

Industry/Entity Type

Pet e-commerce and retail

Font styles to use
Other font styles liked:
• like attached images

Requirements
Nice to have
• light background, eco friendly

```html
<!DOCTYPE html>
<html lang="en">
<head>
<meta charset="utf-8">
<title>VELUTRA Mineral Instant Absorber – Pouch Front</title>
<link href="https://fonts.googleapis.com/css2?family=Josefin+Sans:wght@300;400&family=Montserrat:wght@600;700;800&family=Oswald:wght@500&display=swap" rel="stylesheet">
<style>
  :root{
    --backdrop:#efe6e6;
    --sage:#b2b495;
    --sage-deep:#a5a787;
    --pouch-white:#ececea;
    --olive-dark:#4a4b3e;
    --ink:#1d1d1b;
    --icon-fill:#f1f1ef;
    --dash:#8c8d7c;
    --photo-a:#6b3a24;
    --photo-b:#7d4a30;
    --photo-c:#5e6168;
  }
  *{box-sizing:border-box;margin:0;padding:0}
  html,body{width:1200px;height:1079px;overflow:hidden;background:var(--backdrop)}
  .canvas{position:relative;width:1200px;height:1079px}
  .pouch{position:absolute;left:285px;top:80px;width:630px;height:920px;border-radius:14px;overflow:hidden;background:var(--pouch-white)}
  .pouch-bands{position:absolute;inset:0}
  .seal-lines{position:absolute;left:40px;right:40px;top:12px;height:80px}
  .brand{position:absolute;left:0;right:0;top:92px;text-align:center;font-family:"Josefin Sans",sans-serif;font-weight:300;font-size:58px;letter-spacing:3px;color:var(--ink)}
  .seal-badge{position:absolute;left:264px;top:166px;width:130px;height:130px}
  .step{position:absolute;width:90px;text-align:center}
  .step svg{display:block;margin:0 auto}
  .step-label{font-family:"Montserrat",sans-serif;font-weight:700;font-size:10px;line-height:12px;color:var(--ink);letter-spacing:.3px;margin-top:6px}
  .descriptor{position:absolute;left:152px;top:390px;font-family:"Montserrat",sans-serif;font-weight:700;font-size:11.5px;line-height:15px;color:var(--ink);letter-spacing:.3px}
  .pet-photo{position:absolute;left:212px;top:460px;width:370px;height:460px;border-radius:46% 46% 0 0/28% 28% 0 0;background:radial-gradient(ellipse at 45% 35%,var(--photo-b) 0%,var(--photo-a) 55%,transparent 56%),linear-gradient(120deg,var(--photo-a) 0%,var(--photo-a) 62%,var(--photo-c) 63%,var(--photo-c) 100%)}
  .benefits{position:absolute;left:70px;top:596px;list-style:none;z-index:2}
  .benefits li{display:flex;align-items:center;height:29.5px;font-family:"Oswald",sans-serif;font-weight:500;font-size:13.5px;color:var(--ink);letter-spacing:.2px}
  .benefits svg{margin-right:7px;flex:none}
  .weight{position:absolute;left:70px;top:750px;font-family:"Montserrat",sans-serif;color:var(--ink);z-index:2}
  .weight-kg{font-weight:800;font-size:44px;line-height:46px}
  .weight-lb{font-weight:800;font-size:21px;line-height:26px}
  .tagline-band{position:absolute;left:0;top:836px;width:335px;height:84px;background:var(--olive-dark);border-top-right-radius:60px;z-index:2}
  .tagline{position:absolute;left:77px;top:878px;font-family:"Oswald",sans-serif;font-weight:500;font-size:11px;color:#fff;letter-spacing:.3px;z-index:3}
</style>
</head>
<body>
<div class="canvas">
  <div class="pouch">
    <svg class="pouch-bands" width="630" height="920" viewBox="0 0 630 920">
      <polygon points="0,0 630,0 630,250 0,585" fill="var(--sage)"/>
      <polygon points="180,639 630,400 630,470 180,709" fill="var(--sage-deep)"/>
    </svg>

    <svg class="seal-lines" viewBox="0 0 550 80" preserveAspectRatio="none">
      <g stroke="#8e9076" stroke-width="1">
        <line x1="0" y1="4" x2="550" y2="4"/><line x1="0" y1="12" x2="550" y2="12"/>
        <line x1="0" y1="20" x2="550" y2="20"/><line x1="0" y1="28" x2="550" y2="28"/>
        <line x1="0" y1="36" x2="550" y2="36"/><line x1="0" y1="44" x2="550" y2="44"/>
        <line x1="0" y1="52" x2="550" y2="52"/><line x1="0" y1="60" x2="550" y2="60"/>
        <line x1="0" y1="68" x2="550" y2="68"/><line x1="0" y1="76" x2="550" y2="76"/>
      </g>
    </svg>

    <h1 class="brand">VELUTRA</h1>

    <svg class="seal-badge" viewBox="0 0 130 130">
      <defs><path id="badge-ring" d="M65,115 A50,50 0 1,1 65,15 A50,50 0 1,1 65,115"/></defs>
      <text font-family="Montserrat, sans-serif" font-weight="600" font-size="11" letter-spacing="2.6" fill="var(--ink)">
        <textPath href="#badge-ring" startOffset="1%">FOR MINERAL INSTANT ABSORBER - </textPath>
      </text>
    </svg>

    <div class="step" style="left:47px;top:268px">
      <svg width="68" height="68" viewBox="0 0 68 68">
        <circle cx="34" cy="34" r="32" fill="none" stroke="var(--dash)" stroke-width="1.2" stroke-dasharray="4 3"/>
        <circle cx="34" cy="34" r="26" fill="var(--icon-fill)"/>
        <path d="M24 40 l6-12 l14-6 l2 3 l-10 5 l-2 8 z" fill="none" stroke="var(--ink)" stroke-width="1.3" stroke-linejoin="round"/>
        <circle cx="28" cy="46" r="1.2" fill="var(--ink)"/><circle cx="32" cy="49" r="1.2" fill="var(--ink)"/><circle cx="26" cy="51" r="1.2" fill="var(--ink)"/>
      </svg>
      <div class="step-label">SPRINKLE</div>
    </div>

    <div class="step" style="left:137px;top:270px">
      <svg width="68" height="68" viewBox="0 0 68 68">
        <circle cx="34" cy="34" r="32" fill="none" stroke="var(--dash)" stroke-width="1.2" stroke-dasharray="4 3"/>
        <circle cx="34" cy="34" r="26" fill="var(--icon-fill)"/>
        <g fill="none" stroke="var(--ink)" stroke-width="1.4">
          <line x1="25" y1="20" x2="43" y2="20"/><line x1="25" y1="48" x2="43" y2="48"/>
          <path d="M27 20 c0 9 14 9 14 14 c0 5 -14 5 -14 14"/><path d="M41 20 c0 9 -14 9 -14 14 c0 5 14 5 14 14"/>
        </g>
      </svg>
      <div class="step-label">WAIT 1–5<br>MIN</div>
    </div>

    <div class="step" style="left:51px;top:375px">
      <svg width="68" height="68" viewBox="0 0 68 68">
        <circle cx="34" cy="34" r="32" fill="none" stroke="var(--dash)" stroke-width="1.2" stroke-dasharray="4 3"/>
        <circle cx="34" cy="34" r="26" fill="var(--icon-fill)"/>
        <g fill="none" stroke="var(--ink)" stroke-width="1.4" stroke-linejoin="round">
          <line x1="44" y1="18" x2="36" y2="32"/>
          <path d="M33 30 l8 5 l-6 12 l-10 -6 z"/>
        </g>
        <circle cx="22" cy="34" r="1.3" fill="var(--ink)"/><circle cx="25" cy="38" r="1.3" fill="var(--ink)"/><circle cx="20" cy="40" r="1.3" fill="var(--ink)"/>
      </svg>
      <div class="step-label">SWEEP</div>
    </div>

    <p class="descriptor">MINERAL INSTANT<br>ABSORBER FOR<br>DOGS &amp; CATS</p>

    <div class="pet-photo" role="img" aria-label="Photo of a chocolate Labrador dog with a grey British Shorthair cat in front, both looking at the viewer"></div>

    <ul class="benefits">
      <li><svg width="18" height="18" viewBox="0 0 18 18"><circle cx="9" cy="9" r="8" fill="none" stroke="var(--ink)" stroke-width="1.2"/><line x1="3.5" y1="14.5" x2="14.5" y2="3.5" stroke="var(--ink)" stroke-width="1.2"/></svg>FRAGRANCE-FREE</li>
      <li><svg width="18" height="18" viewBox="0 0 18 18"><circle cx="9" cy="9" r="8" fill="none" stroke="var(--ink)" stroke-width="1.2"/><path d="M9 13 c-4 -2 -4 -6 0 -8 c4 2 4 6 0 8 z" fill="none" stroke="var(--ink)" stroke-width="1.1"/></svg>100 % MINERAL</li>
      <li><svg width="18" height="18" viewBox="0 0 18 18"><circle cx="9" cy="9" r="8" fill="none" stroke="var(--ink)" stroke-width="1.2"/><path d="M6 13 c-2-3 2-5 0-8 M9 13 c-2-3 2-5 0-8 M12 13 c-2-3 2-5 0-8" fill="none" stroke="var(--ink)" stroke-width="1"/></svg>ODOR-BINDING</li>
      <li><svg width="18" height="18" viewBox="0 0 18 18"><circle cx="9" cy="9" r="8" fill="none" stroke="var(--ink)" stroke-width="1.2"/><circle cx="9" cy="9" r="3" fill="var(--ink)"/><line x1="3.5" y1="14.5" x2="14.5" y2="3.5" stroke="var(--ink)" stroke-width="1.2"/></svg>LOW-DUST</li>
    </ul>

    <div class="weight">
      <div class="weight-kg">1 KG</div>
      <div class="weight-lb">2.2 LB</div>
    </div>

    <div class="tagline-band"></div>
    <p class="tagline">NATURAL MINERAL POWER FOR QUICK CLEANUPS.</p>
  </div>
</div>
</body>
</html>
```